Happy Birthday Cards (from Law Firm)

Need classy, professional AND polished Happy Birthday Cards from law firm.

Please tie in the firm logo and colors somewhere with the picture on front or inside(but not used too many times)

Include company logo somewhere on the card, firm name (Verona Pask Law, PLLC) www.veronapasklaw.com
Updates

Reason: Thank you for your patience. Had a family emergency.

Target Market(s)

Law firm clients ages 30 - 99

Industry/Entity Type

Law Firm

Font styles to use
Serif
Sans Serif
Decorative
Script

Requirements
Must have
• Must be classy, elegant, professional, polished from a business
• Birthday wish or message - you suggest one.
• For example "Enjoy every moment of your life. May everyday bring something new and exciting for you. May your birthday be as amazing as you."
Nice to have
• Would like several birthday card templates (for male/for female); traditional/fun

```html
<!DOCTYPE html>
<html lang="en">
<head>
<meta charset="utf-8">
<title>Birthday Card – Verona Pask Law, PLLC</title>
<link rel="stylesheet" href="https://fonts.googleapis.com/css2?family=Lora:ital,wght@1,600&family=Yellowtail&display=swap">
<style>
  :root {
    --page-bg: #ecebe8;
    --card-aqua: #9fd3d9;
    --card-aqua-light: #c4e6ea;
    --card-aqua-deep: #86c4cc;
    --ink-blue: #1f3b9e;
    --window-white: #f7f7f7;
    --window-shade: #d9dcdd;
    --firm-teal: #3f8fa6;
    --shelf: #dff1f3;
  }
  * { box-sizing: border-box; margin: 0; padding: 0; }
  html, body { width: 1200px; height: 800px; overflow: hidden; }
  body {
    background: var(--page-bg);
    position: relative;
    font-family: "Lora", Georgia, serif;
  }
  .card-panel {
    position: absolute;
    top: 150px;
    width: 340px;
    height: 500px;
    background: linear-gradient(160deg, var(--card-aqua-light) 0%, var(--card-aqua) 55%, var(--card-aqua-deep) 100%);
    overflow: hidden;
    box-shadow: 0 6px 18px rgba(0,0,0,0.12);
  }
  .inside-left  { left: 60px; }
  .inside-right { left: 400px; border-left: 1px solid rgba(0,0,0,0.08); }
  .front-cover  { left: 800px; }

  .photo-window { position: absolute; inset: 0; }
  .firm-name {
    position: absolute;
    left: 40px;
    top: 225px;
    width: 200px;
    font-family: "Lora", Georgia, serif;
    font-style: italic;
    font-weight: 600;
    font-size: 17px;
    color: var(--firm-teal);
    text-align: center;
    line-height: 1.25;
  }

  .birthday-message {
    position: absolute;
    top: 60px;
    left: 0; right: 0;
    text-align: center;
    color: var(--ink-blue);
    font-style: italic;
    font-weight: 600;
    font-size: 18px;
    line-height: 1.3;
    padding: 0 30px;
  }
  .birthday-message p + p { margin-top: 20px; }

  .cupcake-photo {
    position: absolute;
    left: 0; right: 0; bottom: 0;
    height: 150px;
    background: linear-gradient(180deg, rgba(159,211,217,0) 0%, rgba(159,211,217,0) 30%, transparent 30%),
      linear-gradient(90deg, #8a55c8 0%, #d3508f 22%, #e0d64a 44%, #7ec95a 66%, #5cb3dc 88%);
    opacity: 0.75;
  }
  .cupcake-photo::after {
    content: "";
    position: absolute;
    left: 0; right: 0; bottom: 0;
    height: 36px;
    background: var(--shelf);
  }

  .cover-title {
    position: absolute;
    top: 70px;
    left: 0; right: 0;
    text-align: center;
    font-family: "Yellowtail", "Brush Script MT", cursive;
    font-weight: 400;
    color: var(--ink-blue);
    font-size: 80px;
    line-height: 0.95;
    text-shadow: 2px 2px 0 #fff, -2px -2px 0 #fff, 2px -2px 0 #fff, -2px 2px 0 #fff, 3px 5px 6px rgba(0,0,0,0.25);
  }
</style>
</head>
<body>
  <section class="card-panel inside-left">
    <svg class="photo-window" width="340" height="500" viewBox="0 0 340 500" aria-hidden="true">
      <path d="M32 40 Q32 24 48 24 L230 24 Q250 24 244 60 Q228 150 250 250 Q272 350 250 440 Q246 470 220 470 L48 470 Q32 470 32 454 Z"
            fill="var(--window-white)" stroke="var(--window-shade)" stroke-width="4"/>
    </svg>
    <p class="firm-name">Verona Pask Law, PLLC</p>
  </section>

  <section class="card-panel inside-right">
    <div class="birthday-message">
      <p>Wishing you a<br>wonderful birthday!</p>
      <p>May your day<br>be filled with lots of love,<br>peace, and all the<br>happiness you deserve!</p>
    </div>
    <div class="cupcake-photo" role="img" aria-label="Row of colourful cupcakes with lit sparklers"></div>
  </section>

  <section class="card-panel front-cover">
    <h1 class="cover-title">Happy<br>Birthday</h1>
    <div class="cupcake-photo" role="img" aria-label="Row of colourful cupcakes with lit sparklers"></div>
  </section>
</body>
</html>
```